New Business Cards for NYC Salon

We are updating all of our cards. 7142-2869-4417 is my account number. We put names of our stylists on their cards. The back should include appointment space. Were looking for something more sleek and modern. Black/White Silver... or even touches of the orange color on our website which has been our thing for years. The design should communicate professional upscale boutique salon for men and women. Should be able to incorporate design into thank you cards, referral cards, brochure and postcards. The file is a zip file...we like the stacked ones black or white or the side versions.

Industry/Entity Type

Beauty Salon

Contact Information for Business Card

Marcus John's Salon313 W. 53rd Street, New York NY 10019 212-736-4852 info@marcusvalesalon.example www.marcusvalesalon.example

Font styles to use
Other font styles liked:
• trajan

Requirements
Must have
• we print a different card for every person in the salon. Begin by designing with the name Marcus. We will change it with every employee when printing. Must have a space for appointment date and time.
Nice to have
• Were looking to move towards the stacked or side placed logo but not opposed to utilizing the circular.
Should not have
• Photos

```html
<!DOCTYPE html>
<html lang="en">
<head>
<meta charset="utf-8">
<title>Marcus Vale's Salon – Business Cards</title>
<link href="https://fonts.googleapis.com/css2?family=Cinzel:wght@400;600&family=Crimson+Text:wght@400;700&display=swap" rel="stylesheet">
<style>
  :root{
    --canvas:#d9d6d1;
    --ink:#1d1b1c;
    --charcoal:#2b2829;
    --silver-light:#ffffff;
    --silver-mid:#e6e6e6;
    --silver-dark:#c9c9c9;
    --grey-text:#8e8b8c;
    --white-text:#f4f2f2;
    --card-shadow:0 10px 28px rgba(0,0,0,.28);
  }
  *{box-sizing:border-box;margin:0;padding:0}
  html,body{width:1200px;height:1023px;overflow:hidden;background:var(--canvas)}
  .card{
    position:absolute;left:206px;width:788px;height:450px;
    border-radius:6px;overflow:hidden;box-shadow:var(--card-shadow);
  }
  .card--front{top:40px}
  .card--back{top:533px;background:var(--ink)}

  /* Front */
  .front__bg{position:absolute;inset:0}
  .front__info{
    position:absolute;left:56px;top:50px;width:430px;color:var(--white-text);
    font-family:"Cinzel",serif;
  }
  .front__label{font-size:17px;letter-spacing:.5px;color:var(--grey-text);margin-bottom:20px}
  .front__stylists{font-size:24px;line-height:1.3;margin-bottom:34px}
  .contact{list-style:none;font-family:"Crimson Text",serif;font-size:19px;letter-spacing:.3px;text-transform:uppercase}
  .contact li{display:flex;align-items:center;gap:12px;height:30px}
  .contact svg{width:18px;height:18px;flex:none}
  .front__address{margin-top:28px;font-family:"Crimson Text",serif;font-size:19px;text-transform:uppercase;line-height:1.3}
  .front__brand{
    position:absolute;right:40px;top:0;height:100%;width:240px;
    display:flex;align-items:center;justify-content:center;
  }
  .brand-name{
    font-family:"Crimson Text",serif;font-weight:400;font-size:30px;
    text-align:center;line-height:1.25;color:var(--ink);
  }

  /* Back */
  .back__panel{
    position:absolute;left:0;top:0;bottom:0;width:360px;
    background:linear-gradient(120deg,var(--silver-light),var(--silver-mid) 60%,var(--silver-dark));
    border-radius:0 40px 40px 0;
  }
  .appointment{
    position:absolute;left:38px;top:54px;width:290px;font-family:"Crimson Text",serif;color:var(--ink);
  }
  .appointment__title{font-weight:700;font-size:30px;margin-bottom:44px}
  .field{display:flex;align-items:flex-end;gap:6px;font-size:20px;text-transform:uppercase;height:68px}
  .field__line{flex:1;border-bottom:2px dotted var(--ink);margin-bottom:6px}
  .back__brand{
    position:absolute;left:360px;right:0;top:0;bottom:0;
    display:flex;align-items:center;justify-content:center;
  }
  .back__brand .brand-name{color:var(--grey-text);font-size:36px}
</style>
</head>
<body>

<section class="card card--front" aria-label="Business card front">
  <svg class="front__bg" width="788" height="450" viewBox="0 0 788 450" aria-hidden="true">
    <defs>
      <linearGradient id="silver" x1="0" y1="0" x2="1" y2="1">
        <stop offset="0" stop-color="#ffffff"/>
        <stop offset=".6" stop-color="#ececec"/>
        <stop offset="1" stop-color="#cfcfcf"/>
      </linearGradient>
    </defs>
    <rect width="788" height="450" fill="url(#silver)"/>
    <path d="M0 0 H500 Q560 225 500 450 H0 Z" fill="#2b2829"/>
  </svg>

  <div class="front__info">
    <p class="front__label">Individualized for each stylist:</p>
    <p class="front__stylists">Marcus, Lena, Iris,<br>Josephine, Rolando, Nora</p>
    <ul class="contact">
      <li><svg viewBox="0 0 24 24"><path fill="#f4f2f2" d="M6.6 10.8a15 15 0 0 0 6.6 6.6l2.2-2.2c.3-.3.7-.4 1-.2 1.1.4 2.3.6 3.6.6.6 0 1 .4 1 1V20c0 .6-.4 1-1 1A17 17 0 0 1 3 4c0-.6.4-1 1-1h3.5c.6 0 1 .4 1 1 0 1.3.2 2.5.6 3.6.1.3 0 .7-.2 1z"/></svg>212-736-4852</li>
      <li><svg viewBox="0 0 24 24"><rect x="2" y="5" width="20" height="14" rx="1" fill="#f4f2f2"/><path d="M2 5l10 8 10-8" fill="none" stroke="#2b2829" stroke-width="1.6"/></svg>info@marcusvalesalon.example</li>
      <li><svg viewBox="0 0 24 24"><circle cx="12" cy="12" r="10" fill="#f4f2f2"/><path d="M2 12h20M12 2c3 3 3 17 0 20M12 2c-3 3-3 17 0 20" fill="none" stroke="#2b2829" stroke-width="1.4"/></svg>www.marcusvalesalon.example</li>
    </ul>
    <p class="front__address">742 E. 61st Street<br>New York NY 10065</p>
  </div>

  <div class="front__brand">
    <p class="brand-name">Marcus Vale's<br>Salon</p>
  </div>
</section>

<section class="card card--back" aria-label="Business card back">
  <div class="back__panel">
    <div class="appointment">
      <p class="appointment__title">Next Appointment</p>
      <div class="field"><span>Name</span><span class="field__line"></span></div>
      <div class="field"><span>Date</span><span class="field__line"></span></div>
      <div class="field"><span>Time</span><span class="field__line"></span></div>
    </div>
  </div>
  <div class="back__brand">
    <p class="brand-name">Marcus Vale's<br>Salon</p>
  </div>
</section>

</body>
</html>
```